Austrian finance und insurance broker needs business card design

We Need a serious looking Design for Business Card. we consult private and corporates customers in finance and insurance questions. the final design should express security and experience. We consult customers in questions of loans, Investments and insurance and have a wide range of Banks to offer. We compare several offers and select the best for our customers.

Target Market(s)

private and coporate customers with efforts in Money and insurance

Industry/Entity Type

Insurance Broker

Contact Information for Business Card

Bernhard Aigner
Geschäftsführer
staatl. geprüfter Vermögensberater und Versicherungsmakler
Tel: 0664 521 8409
office@der-brandl.at
www.der-brandl.at
Leopold Hainz Gasse 14
2183 Melkstetten
GISA Nr. 48270315 u. 51736048 (backside)

Font styles to use
Serif
Sans Serif

Requirements
Must have
• logo (designcrowd zip) and all Details
Nice to have
• makler logo design, maybe a 2 coloured Version is possible

```html
<!DOCTYPE html>
<html lang="de">
<head>
<meta charset="utf-8">
<title>Aigner Vermögensberatung – Visitenkarte</title>
<link rel="stylesheet" href="https://fonts.googleapis.com/css2?family=Quicksand:wght@700&family=Lato:wght@400;700&display=swap">
<style>
  :root{
    --blue:#1a56b8;
    --card-light:#efefef;
    --text-grey:#4a4a4a;
    --rule-grey:#6b6b6b;
    --faint:#e2e2e2;
    --seal-red:#c81e2b;
    --white:#ffffff;
    --stage:#d9d9d9;
  }
  *{box-sizing:border-box;margin:0;padding:0}
  html,body{width:1200px;height:896px;overflow:hidden;background:var(--stage)}
  .stage{width:1200px;height:896px;display:flex;flex-direction:column;align-items:center;justify-content:center;gap:24px}
  .card{position:relative;width:640px;height:414px;overflow:hidden;box-shadow:0 6px 18px rgba(0,0,0,.18)}

  /* front */
  .card--front{background:var(--card-light)}
  .card--front .deco-ring{position:absolute;left:140px;top:-60px;width:380px;height:380px;border-radius:50%;border:14px solid var(--faint)}
  .card--front .edge-band{position:absolute;left:0;right:0;bottom:0;height:14px;background:var(--blue)}
  .brand{position:absolute;left:300px;top:74px;display:flex;align-items:center;gap:14px}
  .brand__mark{display:flex;align-items:center;gap:8px;font-family:'Quicksand',sans-serif;font-weight:700;font-size:24px;color:var(--blue)}
  .brand__dot{width:18px;height:18px;border-radius:50%;background:var(--blue)}
  .brand__divider{width:2px;height:70px;background:var(--rule-grey)}
  .brand__name{font-family:'Quicksand',sans-serif;font-weight:700;font-size:20px;color:var(--blue);line-height:1.1}
  .brand__name small{font-size:13px}
  .brand__claim{font-family:'Lato',sans-serif;font-size:13px;color:var(--text-grey);margin-top:4px}

  .person{position:absolute;left:40px;top:170px}
  .person__name{font-family:'Quicksand',sans-serif;font-weight:700;font-size:24px;color:var(--blue)}
  .person__role{font-family:'Lato',sans-serif;font-size:15px;color:var(--text-grey);line-height:1.35;margin-top:6px}
  .name-rule{position:absolute;left:262px;right:40px;top:190px;height:1px;background:var(--rule-grey)}

  .contact{position:absolute;right:40px;bottom:52px;text-align:right;font-family:'Lato',sans-serif;font-size:16px;color:var(--text-grey);line-height:1.45}
  .contact__rule{position:absolute;right:40px;width:250px;bottom:148px;height:1px;background:var(--rule-grey)}
  .contact li{list-style:none;display:flex;align-items:center;justify-content:flex-end;gap:8px}
  .contact svg{width:14px;height:14px;fill:var(--blue)}

  /* back */
  .card--back{background:var(--blue)}
  .back__gisa{position:absolute;left:36px;top:36px;font-family:'Lato',sans-serif;font-size:17px;color:var(--white)}
  .back__white-band{position:absolute;left:0;right:0;top:92px;height:150px;background:var(--white)}
  .partner-badge{position:absolute;left:70px;top:112px;width:110px;height:110px;border-radius:50%;background:var(--seal-red)}
  .back__address{position:absolute;left:36px;top:300px;font-family:'Lato',sans-serif;font-size:19px;color:var(--white)}
  .back__emblem{position:absolute;left:390px;top:96px;width:330px;height:330px;border-radius:50%;background:var(--blue);border:12px solid var(--white);display:flex;align-items:center;padding-left:44px;font-family:'Quicksand',sans-serif;font-weight:700;font-size:56px;color:var(--white)}
</style>
</head>
<body>
<main class="stage">

  <section class="card card--front" aria-label="Visitenkarte Vorderseite">
    <div class="deco-ring"></div>
    <div class="brand">
      <div class="brand__mark"><span class="brand__dot"></span>Aigner</div>
      <div class="brand__divider"></div>
      <div>
        <div class="brand__name">Vermögensberatung <small>GmbH</small></div>
        <div class="brand__claim">Finanzieren, Versichern, Vorsorgen</div>
      </div>
    </div>

    <div class="person">
      <h1 class="person__name">Bernhard Aigner</h1>
      <p class="person__role">Geschäftsführer<br>staatl. geprüfter Vermögensberater<br>und Versicherungsmakler</p>
    </div>
    <div class="name-rule"></div>

    <div class="contact__rule"></div>
    <ul class="contact">
      <li>0664 521 8409
        <svg viewBox="0 0 24 24" aria-hidden="true"><path d="M6.6 10.8a15 15 0 006.6 6.6l2.2-2.2c.3-.3.7-.4 1-.2 1.1.4 2.3.6 3.6.6.6 0 1 .4 1 1V20c0 .6-.4 1-1 1A17 17 0 013 4c0-.6.4-1 1-1h3.5c.6 0 1 .4 1 1 0 1.3.2 2.5.6 3.6.1.3 0 .7-.2 1z"/></svg></li>
      <li>office@der-brandl.at
        <svg viewBox="0 0 24 24" aria-hidden="true"><path d="M2 5h20v14H2zm2 2v.5l8 5 8-5V7l-8 5z"/></svg></li>
      <li>www.der-brandl.at
        <svg viewBox="0 0 24 24" aria-hidden="true"><circle cx="12" cy="12" r="10"/></svg></li>
    </ul>
    <div class="edge-band"></div>
  </section>

  <section class="card card--back" aria-label="Visitenkarte Rückseite">
    <p class="back__gisa">GISA Nr: 48270315 u. 51736048</p>
    <div class="back__white-band"></div>
    <div class="partner-badge" role="img" aria-label="Partnerabzeichen Versicherungsmakler"></div>
    <p class="back__address">Leopold Hainz Gasse 14 &nbsp;2183 Melkstetten</p>
    <div class="back__emblem">Aigner</div>
  </section>

</main>
</body>
</html>
```